I need a label with logo to go on jars of honey.
Label size 70mm x 70mm
The front label should say :
The Kestrel Honey Co. (logo)
Torvale Honey
400g
The back label:
Would have nutritional information
And our address
You can see from the uploaded files the styles I prefer, I have uploaded a photo of the honey product too. The background of the logo doesn't have to be white. I would like to develop a color scheme that would look nice against the color of the honey.
The Kestrel Honey Co. / The Kestrel Honey Company

```html
<!DOCTYPE html>
<html lang="en">
<head>
<meta charset="utf-8">
<title>The Kestrel Honey Co. – Torvale Honey Label</title>
<link href="https://fonts.googleapis.com/css2?family=Indie+Flower&display=swap" rel="stylesheet">
<style>
  :root {
    --canvas-bg: #ffffff;
    --label-edge: #efdca6;
    --label-warm: #e2b338;
    --label-core: #d5a126;
    --label-right: #e7c97f;
    --ink: #231f1a;
  }
  * { margin: 0; padding: 0; box-sizing: border-box; }
  html, body {
    width: 1200px;
    height: 849px;
    overflow: hidden;
    background: var(--canvas-bg);
  }
  .canvas {
    position: relative;
    width: 1200px;
    height: 849px;
    background: var(--canvas-bg);
  }
  .jar-label {
    position: absolute;
    left: 291px;
    top: 74px;
    width: 618px;
    height: 700px;
    background: linear-gradient(90deg,
      var(--label-edge) 0%,
      var(--label-warm) 22%,
      var(--label-core) 50%,
      var(--label-warm) 75%,
      var(--label-right) 100%);
    color: var(--ink);
    font-family: "Indie Flower", cursive;
  }
  .top-rule {
    position: absolute;
    left: 0;
    right: 0;
    top: 80px;
    height: 2px;
    background: var(--ink);
    opacity: 0.85;
  }
  .brand-name {
    position: absolute;
    left: 0;
    right: 0;
    top: 185px;
    text-align: center;
    font-size: 44px;
    line-height: 58px;
    font-weight: 400;
    color: var(--ink);
  }
  .product-name {
    position: absolute;
    left: 0;
    right: 0;
    top: 527px;
    text-align: center;
    font-size: 36px;
    line-height: 44px;
  }
  .weight-row {
    position: absolute;
    left: 0;
    right: 0;
    top: 600px;
    display: flex;
    align-items: center;
    gap: 16px;
  }
  .weight-row .rule {
    flex: 1;
    height: 1.5px;
    background: var(--ink);
    opacity: 0.8;
  }
  .net-weight {
    font-size: 32px;
    line-height: 40px;
  }
</style>
</head>
<body>
  <main class="canvas">
    <section class="jar-label" aria-label="Front label">
      <div class="top-rule"></div>
      <h1 class="brand-name">The<br>Kestrel<br>Honey<br>Co.</h1>
      <p class="product-name">Torvale Honey</p>
      <div class="weight-row">
        <span class="rule"></span>
        <span class="net-weight">400g</span>
        <span class="rule"></span>
      </div>
    </section>
  </main>
</body>
</html>
```